Einladungskarten Design
Zielgruppe
Die Zielgruppe besteht aus allen Privatpersonen, die eine Feier planen und auf der Suche nach individuellen, professionell gestalteten Einladungskarten für Ihre Feier sind:
Hochzeit
Geburtstag (meistens runde Geburtstage)
Mottoparty´s
Danksagung zur Gebur
Aufgabenstellung
Für das Online-Angebot www.kartenfreude-atelier.de werden kreative Vorschläge für Einladungskarten und Danksagungskarten in verschiedenen Kategorien gesucht: Hochzeit, Geburtstag, Party, Mottoparty, Geburt und weitere Themen. Das Thema ist wählbar, da für alle Kategorien neue, frische Entwürfe benötigt werden.
Dies ist kein Wettbewerb im herkömmlichen Sinne, da es keinen einzelnen Gewinner gibt. Jeder Kartenentwurf, der für das Online Angebot ausgewählt wird, wird mit 100,00 Eur honoriert.
Voraussetzung für die Honorarzahlung ist das Einverständnis der Veröffentlichung und die Übertragung der Nutzungsrechte.

```html
<!DOCTYPE html>
<html lang="de">
<head>
<meta charset="utf-8">
<title>Hochzeitseinladung Ida &amp; Paul</title>
<link rel="stylesheet" href="https://fonts.googleapis.com/css2?family=EB+Garamond:ital,wght@0,400;1,400&family=Questrial&display=swap">
<style>
  :root {
    --stage: #000000;
    --olive: #9a8b00;
    --olive-edge: #6b5e00;
    --olive-deep: #3b3600;
    --olive-shadow: #8a7b00;
    --gold: #c9ae00;
    --amber-dark: #8f7700;
    --paper: #ffffff;
    --pale-yellow: #fbe98f;
    --sand: #c9b98c;
    --sage: #d9e0c8;
    --serif: "EB Garamond", Georgia, serif;
    --sans: "Questrial", "Helvetica Neue", Arial, sans-serif;
  }
  html, body {
    margin: 0;
    padding: 0;
    width: 1200px;
    height: 880px;
    overflow: hidden;
    background: var(--stage);
  }
  .canvas {
    position: relative;
    width: 1200px;
    height: 880px;
  }
  .card {
    position: absolute;
    box-sizing: border-box;
    overflow: hidden;
    border: 2px solid var(--olive-edge);
  }
  .card-front { left: 30px; top: 24px; width: 575px; height: 258px; background: var(--olive); }
  .card-inside { left: 28px; top: 310px; width: 1150px; height: 257px; background: var(--paper); }
  .card-back { left: 28px; top: 597px; width: 574px; height: 255px; background: var(--olive); }
  .circles { position: absolute; left: 0; top: 0; }

  /* front */
  .front-amp {
    position: absolute;
    left: 360px;
    top: -30px;
    font-family: var(--serif);
    font-size: 300px;
    line-height: 1;
    color: var(--olive-shadow);
  }
  .front-title {
    position: absolute;
    left: 20px;
    top: 74px;
    margin: 0;
    font-family: var(--sans);
    font-weight: 400;
    color: var(--olive);
    -webkit-text-stroke: 0.8px var(--paper);
    white-space: nowrap;
  }
  .front-title .big { font-size: 70px; letter-spacing: 2px; }
  .front-title .small { font-size: 42px; margin-left: 8px; letter-spacing: 1.5px; }
  .name-tag {
    position: absolute;
    left: 362px;
    top: 88px;
    width: 220px;
    height: 68px;
    box-sizing: border-box;
    background: var(--paper);
    border: 2px solid var(--olive-edge);
    border-right: none;
    font-family: var(--serif);
    color: var(--olive);
  }
  .name-tag .first { position: absolute; left: 12px; top: 12px; font-size: 20px; }
  .name-tag .amp { position: absolute; left: 62px; top: -6px; font-size: 62px; color: var(--olive-deep); }
  .name-tag .second { position: absolute; left: 126px; top: 26px; font-size: 20px; }

  /* inside */
  .inside-amp {
    position: absolute;
    left: 162px;
    top: 28px;
    font-family: var(--serif);
    font-size: 245px;
    line-height: 1;
    color: var(--sage);
  }
  .couple { font-family: var(--serif); color: var(--olive); font-size: 90px; line-height: 1; position: absolute; margin: 0; font-weight: 400; }
  .couple-first { left: 82px; top: 74px; }
  .couple-second { left: 297px; top: 134px; }
  .divider { position: absolute; left: 573px; top: 0; width: 1px; height: 100%; background: var(--olive-edge); opacity: .7; }
  .invite-lead {
    position: absolute;
    left: 608px;
    top: 28px;
    margin: 0;
    font-family: var(--serif);
    font-size: 37px;
    letter-spacing: 2px;
    color: var(--olive);
    font-weight: 400;
  }
  .details {
    position: absolute;
    left: 697px;
    top: 106px;
    margin: 0;
    display: grid;
    grid-template-columns: 80px auto;
    row-gap: 1px;
    font-family: var(--sans);
    font-size: 33px;
    line-height: 39px;
    letter-spacing: 1.5px;
    color: var(--olive);
  }
  .details dt, .details dd { margin: 0; }
</style>
</head>
<body>
<main class="canvas">

  <section class="card card-front" aria-label="Vorderseite">
    <svg class="circles" width="575" height="258" aria-hidden="true">
      <circle cx="30" cy="6" r="68" fill="var(--gold)"/>
      <circle cx="107" cy="-17" r="63" fill="var(--amber-dark)" opacity=".75"/>
    </svg>
    <span class="front-amp" aria-hidden="true">&amp;</span>
    <h1 class="front-title"><span class="big">Wir</span><span class="small">heiraten</span></h1>
    <div class="name-tag">
      <span class="first">Ida</span>
      <span class="amp">&amp;</span>
      <span class="second">Paul</span>
    </div>
  </section>

  <section class="card card-inside" aria-label="Innenseite">
    <svg class="circles" width="574" height="257" aria-hidden="true">
      <circle cx="-14" cy="28" r="100" fill="var(--pale-yellow)"/>
      <circle cx="166" cy="-33" r="108" fill="var(--sand)" opacity=".85"/>
    </svg>
    <span class="inside-amp" aria-hidden="true">&amp;</span>
    <h2 class="couple couple-first">Ida</h2>
    <h2 class="couple couple-second">Paul</h2>
    <div class="divider"></div>
    <p class="invite-lead">laden zur Hochzeit...</p>
    <dl class="details">
      <dt>am:</dt><dd>20.09.2009</dd>
      <dt>um:</dt><dd>11.30 Uhr</dd>
      <dt>im:</dt><dd>Schloss Lindenhain</dd>
    </dl>
  </section>

  <section class="card card-back" aria-label="Rückseite">
    <svg class="circles" width="574" height="255" aria-hidden="true">
      <circle cx="240" cy="120" r="61" fill="var(--gold)"/>
      <circle cx="330" cy="120" r="61" fill="var(--amber-dark)" opacity=".8"/>
    </svg>
  </section>

</main>
</body>
</html>
```